Picture Ads

We need some banner ads for our home business opportunity, we are evolving from text to picture ads. I have added some examples of what other distributors are using. We are looking for something really eye catching with some good key words and nice bright colours and to include our photo (attached)
Key words to include:
Booming online business
Personal Development and Leadership Industry
Earn an executive income from home
Simple 3 step system
Make up to $5,000 per sale
Not MLM
The size needs to be: 1000 x 35 pixels
13.9 x 4.75 Inches
35.3 x 11.1 cm
I think different platforms accept different sizes, not too familiar with it yet, any guidance welcome. I've clicked project for 2 days if that is to prioritise the order?
Many thanks,
Maren

Industry/Entity Type

Business

```html
<!DOCTYPE html>
<html lang="en">
<head>
<meta charset="utf-8">
<title>Booming Online Business Banner</title>
<link rel="stylesheet" href="https://fonts.googleapis.com/css2?family=Bebas+Neue&family=Kaushan+Script&family=Questrial&family=Montserrat:wght@700&display=swap">
<style>
  :root {
    --ink-dark: #221c26;
    --plum-deep: #3a2344;
    --violet-band: #8a2fa3;
    --violet-glow: #b04fc8;
    --headline: #ffffff;
    --highlight-yellow: #f4f000;
    --bullet-lilac: #9d92e6;
    --ribbon-dark: #1e1e22;
    --ribbon-mid: #3a3a40;
    --button-black: #000000;
    --frame-white: #ffffff;
  }
  html, body {
    margin: 0;
    padding: 0;
    overflow: hidden;
    background: #ffffff;
  }
  .banner {
    position: relative;
    width: 1200px;
    height: 377px;
    overflow: hidden;
    background:
      radial-gradient(ellipse 420px 90px at 120px 230px, rgba(176,79,200,0.55), transparent 70%),
      linear-gradient(180deg,
        var(--ink-dark) 0%,
        var(--plum-deep) 30%,
        #5a2b6a 36%,
        var(--violet-band) 44%,
        var(--violet-glow) 52%,
        var(--violet-band) 58%,
        #4a2456 66%,
        var(--ink-dark) 78%,
        #17131a 100%);
  }
  .banner::before {
    content: "";
    position: absolute;
    inset: 0;
    background: linear-gradient(90deg, rgba(0,0,0,0) 0%, rgba(0,0,0,0) 55%, rgba(20,10,24,0.45) 100%);
  }
  .headline {
    position: absolute;
    left: 46px;
    top: 4px;
    margin: 0;
    font-family: "Bebas Neue", "Oswald", sans-serif;
    font-weight: 400;
    font-size: 93px;
    line-height: 1;
    letter-spacing: 1px;
    color: var(--headline);
    white-space: nowrap;
  }
  .tagline {
    position: absolute;
    left: 106px;
    top: 92px;
    margin: 0;
    font-family: "Kaushan Script", cursive;
    font-size: 34px;
    line-height: 1.2;
    color: var(--headline);
    white-space: nowrap;
  }
  .offer {
    position: absolute;
    left: 54px;
    top: 172px;
    margin: 0;
    font-family: "Bebas Neue", "Oswald", sans-serif;
    font-size: 71px;
    line-height: 1;
    letter-spacing: 0.5px;
    color: var(--highlight-yellow);
    white-space: nowrap;
  }
  .ribbon {
    position: absolute;
    left: 0;
    top: 252px;
    width: 432px;
    height: 112px;
  }
  .benefits {
    position: absolute;
    left: 56px;
    top: 253px;
    margin: 0;
    padding: 0;
    list-style: none;
    font-family: "Questrial", "Century Gothic", sans-serif;
    font-size: 30px;
    line-height: 35px;
    color: var(--bullet-lilac);
    white-space: nowrap;
  }
  .benefits li {
    display: flex;
    align-items: center;
    gap: 16px;
  }
  .benefits svg {
    width: 19px;
    height: 19px;
    flex: none;
  }
  .portrait-frame {
    position: absolute;
    left: 864px;
    top: -40px;
    width: 480px;
    height: 480px;
    background: var(--frame-white);
    transform: rotate(11deg);
    transform-origin: center;
    box-shadow: -6px 6px 14px rgba(0,0,0,0.45);
  }
  .portrait {
    position: absolute;
    inset: 10px;
    background:
      radial-gradient(circle at 35% 45%, #b88a78 0 14%, transparent 32%),
      radial-gradient(circle at 65% 38%, #c89a6a 0 15%, transparent 34%),
      linear-gradient(135deg, #6a5a52 0%, #3a2c2a 45%, #8a6a50 100%);
  }
  .pointer {
    position: absolute;
    left: 620px;
    top: 306px;
    width: 148px;
    height: 62px;
  }
  .cta {
    position: absolute;
    left: 758px;
    top: 310px;
    width: 442px;
    height: 67px;
    display: flex;
    align-items: center;
    justify-content: center;
    background: var(--button-black);
    font-family: "Montserrat", Arial, sans-serif;
    font-weight: 700;
    font-size: 24px;
    letter-spacing: 0.5px;
    color: #ffffff;
    text-decoration: none;
    white-space: nowrap;
  }
</style>
</head>
<body>
<div class="banner">
  <h1 class="headline">Booming Online Business</h1>
  <p class="tagline">Personal Development and Leadership Industry</p>
  <p class="offer">Make up to $5,000 per sale</p>

  <svg class="ribbon" viewBox="0 0 432 112" aria-hidden="true">
    <defs>
      <linearGradient id="ribbonFill" x1="0" y1="0" x2="1" y2="0">
        <stop offset="0" stop-color="var(--ribbon-mid)"/>
        <stop offset="0.6" stop-color="var(--ribbon-dark)"/>
        <stop offset="1" stop-color="#0e0e10"/>
      </linearGradient>
    </defs>
    <polygon points="0,0 432,0 398,112 0,112" fill="url(#ribbonFill)"/>
  </svg>

  <ul class="benefits">
    <li><svg viewBox="0 0 20 20" aria-hidden="true"><polygon points="10,1 12.6,7.2 19.3,7.6 14.2,11.9 15.8,18.5 10,14.9 4.2,18.5 5.8,11.9 0.7,7.6 7.4,7.2" fill="var(--bullet-lilac)"/></svg>Simple 3 step system</li>
    <li><svg viewBox="0 0 20 20" aria-hidden="true"><polygon points="10,1 12.6,7.2 19.3,7.6 14.2,11.9 15.8,18.5 10,14.9 4.2,18.5 5.8,11.9 0.7,7.6 7.4,7.2" fill="var(--bullet-lilac)"/></svg>Make up to $5,000 per sale</li>
    <li><svg viewBox="0 0 20 20" aria-hidden="true"><polygon points="10,1 12.6,7.2 19.3,7.6 14.2,11.9 15.8,18.5 10,14.9 4.2,18.5 5.8,11.9 0.7,7.6 7.4,7.2" fill="var(--bullet-lilac)"/></svg>Not MLM</li>
  </ul>

  <div class="portrait-frame">
    <div class="portrait" role="img" aria-label="Photo of two smiling women, the business owners"></div>
  </div>

  <svg class="pointer" viewBox="0 0 148 62" aria-hidden="true">
    <defs>
      <linearGradient id="pointerFade" x1="0" y1="0" x2="1" y2="0">
        <stop offset="0" stop-color="#ffffff" stop-opacity="0"/>
        <stop offset="0.6" stop-color="#ffffff" stop-opacity="0.9"/>
        <stop offset="1" stop-color="#ffffff"/>
      </linearGradient>
    </defs>
    <polygon points="0,20 104,20 104,2 146,31 104,60 104,42 0,42" fill="url(#pointerFade)"/>
  </svg>

  <a class="cta" href="#">CLICK HERE FOR MORE INFO</a>
</div>
</body>
</html>
```